Business Card Design

After a corporate career in the finance sector I am now operating on my own as a consultant. I require a simple design, and want a strong card which is targeted at a conservative audience.

Target Market(s)

highly educated senior management, directors of companies, finance sector

Industry/Entity Type

Conservative

Contact Information for Business Card

Ruth Danver
Consultant
Mobile: 0417 862 450
Email: ruth.danv@mailcove.net

Requirements
Should not have
• I don't want the colours green/yellow/brown

```html
<!DOCTYPE html>
<html lang="en">
<head>
<meta charset="utf-8">
<title>Ruth Danver – Business Card</title>
<link href="https://fonts.googleapis.com/css2?family=Teko:wght@500;600&family=Open+Sans:ital,wght@0,400;0,600;1,400&display=swap" rel="stylesheet">
<style>
  :root {
    --purple: #7a2a8c;
    --purple-deep: #5e1a70;
    --purple-light: #9a43ad;
    --ink: #1d1d1f;
    --text: #333333;
    --rule: #9a9a9a;
    --card: #ffffff;
    --backdrop: #e4e2e6;
  }
  * { box-sizing: border-box; margin: 0; padding: 0; }
  html, body { width: 1200px; height: 899px; overflow: hidden; }
  body {
    background: var(--backdrop);
    font-family: "Open Sans", Arial, sans-serif;
    position: relative;
  }
  .card {
    position: absolute;
    width: 510px;
    height: 306px;
    background: var(--card);
    border-radius: 26px;
    overflow: hidden;
    box-shadow: 0 10px 28px rgba(0,0,0,.18);
  }
  .card--front { left: 60px; top: 296px; }
  .card--back  { left: 630px; top: 296px; }

  .card__art { position: absolute; inset: 0; }

  .card__holder {
    position: absolute;
    right: 28px;
    top: 56px;
    text-align: right;
    color: #fff;
  }
  .card__holder-name { font-size: 19px; font-weight: 600; }
  .card__holder-role { font-size: 16px; font-style: italic; }

  .brand { position: absolute; left: 24px; top: 70px; }
  .brand__mark {
    width: 62px; height: 56px;
    background: var(--purple);
    border-radius: 6px;
    margin-left: 44px;
    margin-bottom: 8px;
  }
  .brand__name, .brand__tag {
    font-family: "Teko", "Arial Narrow", sans-serif;
    font-weight: 600;
    font-size: 38px;
    line-height: 30px;
    letter-spacing: 1px;
    text-transform: uppercase;
  }
  .brand__name { color: var(--purple); }
  .brand__tag { color: var(--ink); }

  .contact {
    position: absolute;
    left: 212px;
    top: 152px;
    padding-left: 16px;
    border-left: 1px solid var(--rule);
    font-size: 14px;
    line-height: 19px;
    color: var(--text);
    list-style: none;
  }
  .contact__item { display: flex; align-items: center; gap: 6px; }
  .contact__icon { width: 12px; height: 12px; fill: var(--ink); flex: none; }
  .website {
    position: absolute;
    left: 196px;
    top: 262px;
    font-size: 14px;
    color: var(--text);
  }

  .card--back .brand {
    left: 50%; top: 50%;
    transform: translate(-50%, -50%);
    text-align: center;
  }
  .card--back .brand__mark { margin: 0 auto 10px; }
</style>
</head>
<body>

  <section class="card card--front" aria-label="Business card front">
    <svg class="card__art" viewBox="0 0 510 306" aria-hidden="true">
      <defs>
        <linearGradient id="bandFill" x1="0" y1="0" x2="1" y2="1">
          <stop offset="0" stop-color="#9a43ad"/>
          <stop offset="1" stop-color="#5e1a70"/>
        </linearGradient>
      </defs>
      <path d="M112 0 H510 V128 C400 120 250 70 112 0 Z" fill="url(#bandFill)"/>
      <path d="M96 4 C220 74 380 126 510 146 V138 C380 116 230 64 108 0 Z" fill="#1d1d1f"/>
    </svg>

    <div class="card__holder">
      <p class="card__holder-name">Ruth Danver</p>
      <p class="card__holder-role">Consultant</p>
    </div>

    <div class="brand">
      <div class="brand__mark"></div>
      <p class="brand__name">Ruth Danver</p>
      <p class="brand__tag">Consultant</p>
    </div>

    <ul class="contact">
      <li class="contact__item">214 Harbour Lane, Level 9</li>
      <li class="contact__item">Kestrel Quay</li>
      <li class="contact__item">
        <svg class="contact__icon" viewBox="0 0 12 12"><rect x="3" y="0" width="6" height="12" rx="1.2"/><rect x="4" y="1.5" width="4" height="7" fill="#fff"/></svg>
        0417 862 450
      </li>
      <li class="contact__item">
        <svg class="contact__icon" viewBox="0 0 12 12"><path d="M2.4 0.6 L4.6 0.6 L5.4 3.4 L3.9 4.6 C4.6 6.1 5.9 7.4 7.4 8.1 L8.6 6.6 L11.4 7.4 L11.4 9.6 C11.4 10.6 10.6 11.4 9.6 11.4 C4.6 11.1 0.9 7.4 0.6 2.4 C0.6 1.4 1.4 0.6 2.4 0.6 Z"/></svg>
        0398 214 607
      </li>
      <li class="contact__item">
        <svg class="contact__icon" viewBox="0 0 12 12"><rect x="0" y="2" width="12" height="8" rx="1"/><path d="M0.6 2.6 L6 6.6 L11.4 2.6" fill="none" stroke="#fff" stroke-width="1"/></svg>
        ruth.danv@mailcove.net
      </li>
    </ul>

    <p class="website">www.danverconsulting.net</p>
  </section>

  <section class="card card--back" aria-label="Business card back">
    <div class="brand">
      <div class="brand__mark"></div>
      <p class="brand__name">Ruth Danver</p>
      <p class="brand__tag">Consultant</p>
    </div>
  </section>

</body>
</html>
```